My portfolio needs a makeover! Clean, modern portfolio website needed for tech professional

I need a modern, updated design for my existing portfolio site (https://mirelvoss.folioplace.example/). I am a content professional who has done a lot of different types of content work for big companies. I don't really have a title.

I want to stay simple and clean, but also can be a little whimsical, fun, and a little colorful to go along with the logo I just selected.

I have a domain on Wordpress (mirelvoss.example), but I’d be willing to move my domain to another site for the right design.

I would like it coded/configured and deployed, but I need the ability to update the site myself later to easily switch out my portfolio pieces. I’m not very good at html/xml.

Pages needed:
Home page
Who I am
How to reach me
What I do > By Craft (in the nav, this will be a dropdown under What I Do)
What I do > By Brand (in the nav, this will be a dropdown under What I Do)

Please see Website Design Doc for details!

Requirements
Must have
• Design must include these pages:
1. Homepage
2. Who I Am
3. What I Do
- By Brand
- By Craft
4. How to Reach Me
Nice to have
• Example portfolio sites I like:
https://www.vornaledger.example/
http://lunadrexel.example/
https://www.tjworvan.example/
https://www.orrinbalquist.example/

For my portfolio pieces, I like either tiles or a carousel.

```html
<!DOCTYPE html>
<html lang="en">
<head>
<meta charset="utf-8">
<title>Mirel Voss — Portfolio Pages</title>
<link rel="stylesheet" href="https://fonts.googleapis.com/css2?family=Fira+Sans+Condensed:wght@400;500;600;700&family=Fira+Sans:wght@700;800&display=swap">
<style>
:root{
  --ink:#262626;
  --sidebar:#2a2a2a;
  --paper:#f2ebe3;
  --sky:#4db6e2;
  --white:#ffffff;
  --dot:#111111;
  --muted:#444444;
}
*{margin:0;padding:0;box-sizing:border-box}
html,body{width:1200px;height:2321px;overflow:hidden;background:var(--white)}
body{position:relative;font-family:"Fira Sans Condensed",sans-serif;color:var(--ink)}
.section-label{position:absolute;left:100px;font-family:"Fira Sans",sans-serif;font-weight:800;font-size:27px;letter-spacing:2.5px;color:var(--ink)}
.panel{position:absolute;left:100px;width:1000px;height:625px;background:var(--paper)}
.sidebar{position:absolute;left:0;top:0;width:187px;height:100%;background:var(--sidebar)}
.brand{position:absolute;left:42px;top:50px;display:flex;flex-direction:column;align-items:center;width:106px}
.brand-dot{width:14px;height:14px;border-radius:50%;background:var(--sky);margin-bottom:8px}
.brand-name{font-family:"Fira Sans Condensed",sans-serif;font-weight:600;font-size:17px;letter-spacing:.5px;color:var(--sky);white-space:nowrap}
.nav{list-style:none}
.nav li{position:absolute;left:42px;font-family:"Fira Sans",sans-serif;font-weight:700;font-size:9.5px;letter-spacing:1.2px;color:var(--white);white-space:nowrap}
.nav li.sub{left:55px}
.nav li.active{color:var(--sky)}
.nav svg{vertical-align:middle;margin-left:10px}
.social{position:absolute;width:18px;height:18px;border-radius:50%;background:var(--sky)}
.main{position:absolute;left:187px;top:0;right:0;bottom:0}
.page-title{position:absolute;left:62px;top:38px;font-family:"Fira Sans",sans-serif;font-weight:800;font-size:62px;letter-spacing:3px;line-height:1}
.page-title .accent{color:var(--sky)}
.lede{position:absolute;left:62px;top:110px;width:660px;font-size:19px;font-weight:500;line-height:25px}
.subhead{position:absolute;left:62px;top:112px;font-size:19px;font-weight:500}
.contact{position:absolute;top:242px;width:250px;text-align:center;margin-left:-125px}
.contact-icon{display:block;margin:0 auto 28px}
.contact-label{font-size:18px;font-weight:500;letter-spacing:.3px;margin-bottom:6px}
.contact-link{font-size:15px;color:var(--sky);text-decoration:none}
.contact-link.underline{text-decoration:underline}
.project{position:absolute;top:164px;width:313px}
.project-media{width:313px;height:313px}
.project-title{margin-top:14px;font-size:19px;font-weight:500}
.project-text{margin-top:10px;font-size:11.5px;line-height:19px;color:var(--muted)}
.carousel-dots{position:absolute;left:925px;top:268px;list-style:none}
.carousel-dots li{width:12px;height:12px;border-radius:50%;background:var(--dot);margin-bottom:13px}
.carousel-dots li.current{background:var(--sky)}
</style>
</head>
<body>

<!-- How to reach me -->
<h2 class="section-label" style="top:53px">HOW TO REACH ME</h2>
<section class="panel" style="top:100px">
  <aside class="sidebar">
    <div class="brand"><span class="brand-dot"></span><span class="brand-name">MIREL VOSS</span></div>
    <ul class="nav">
      <li style="top:140px">HOME</li>
      <li style="top:178px">WHO AM I</li>
      <li style="top:215px">WHAT I DO<svg width="8" height="5" viewBox="0 0 8 5"><path d="M1 1l3 3 3-3" fill="none" stroke="#fff" stroke-width="1.2"/></svg></li>
      <li class="active" style="top:253px">HOW TO REACH ME</li>
    </ul>
    <span class="social" style="left:43px;top:293px"></span>
  </aside>
  <div class="main">
    <h1 class="page-title">HOW TO <span class="accent">REACH</span> ME</h1>
    <p class="lede">I’d love to hear from you! If you have questions, comments, or just want to geek out over all things content, please reach out.</p>

    <div class="contact" style="left:157px">
      <svg class="contact-icon" width="62" height="62" viewBox="0 0 62 62"><circle cx="31" cy="31" r="31" fill="#4db6e2"/><rect x="17" y="20" width="28" height="21" rx="3" fill="#fff"/><path d="M18 22l13 10 13-10" fill="none" stroke="#4db6e2" stroke-width="2.5"/></svg>
      <div class="contact-label">EMAIL</div>
      <a class="contact-link" href="mailto:mirel.voss@mailbox.example">mirel.voss@mailbox.example</a>
    </div>
    <div class="contact" style="left:407px">
      <svg class="contact-icon" width="62" height="62" viewBox="0 0 62 62"><circle cx="31" cy="31" r="31" fill="#4db6e2"/></svg>
      <div class="contact-label">NETWORK PROFILE</div>
      <a class="contact-link" href="#">www.netprofile.example/in/mirel-voss/</a>
    </div>
    <div class="contact" style="left:657px">
      <svg class="contact-icon" width="62" height="62" viewBox="0 0 62 62"><circle cx="31" cy="31" r="31" fill="#4db6e2"/><path d="M31 16v26M20 32l11 11 11-11" fill="none" stroke="#fff" stroke-width="6" stroke-linecap="round" stroke-linejoin="round"/></svg>
      <div class="contact-label">DOWNLOAD</div>
      <a class="contact-link underline" href="#">My Resume</a>
    </div>
  </div>
</section>

<!-- By brand -->
<h2 class="section-label" style="top:801px">BY BRAND</h2>
<section class="panel" style="top:848px">
  <aside class="sidebar">
    <div class="brand"><span class="brand-dot"></span><span class="brand-name">MIREL VOSS</span></div>
    <ul class="nav">
      <li style="top:128px">HOME</li>
      <li style="top:166px">WHO AM I</li>
      <li style="top:203px">WHAT I DO<svg width="8" height="5" viewBox="0 0 8 5"><path d="M1 1l3 3 3-3" fill="none" stroke="#fff" stroke-width="1.2"/></svg></li>
      <li class="sub active" style="top:241px">BY BRAND</li>
      <li class="sub" style="top:278px">BY CRAFT</li>
      <li style="top:316px">HOW TO REACH ME</li>
    </ul>
    <span class="social" style="left:39px;top:354px"></span>
  </aside>
  <div class="main">
    <h1 class="page-title">BY <span class="accent">BRAND</span></h1>
    <p class="subhead">Writing &amp; Editing</p>
    <article class="project" style="left:63px">
      <div class="project-media" role="img" aria-label="Project image: decorated gingerbread cookies on a white card" style="background:linear-gradient(180deg,#f7f7f7 0%,#e9e6e1 50%,#d9a86a 52%,#e9e6e1 70%,#f7f7f7 100%)"></div>
      <h3 class="project-title">Project One</h3>
      <p class="project-text">Lorem ipsum dolor sit amet, consectetur adipiscing elit, sed do eiusmod tempor incididunt ut labore et dolore magna aliqua. Quis ipsum suspendisse ultrices gravida. Risus commodo viverra maecenas accumsan lacus vel facilisis.</p>
    </article>
    <article class="project" style="left:394px">
      <div class="project-media" role="img" aria-label="Project image: screenshot of the Voyagera cruise questions web page" style="background:linear-gradient(180deg,#3a6fb0 0%,#3a6fb0 12%,#f4f6f9 13%,#e6ecf3 100%)"></div>
      <h3 class="project-title">Project Two</h3>
      <p class="project-text">Lorem ipsum dolor sit amet, consectetur adipiscing elit, sed do eiusmod tempor incididunt ut labore et dolore magna aliqua. Quis ipsum suspendisse ultrices gravida. Risus commodo viverra maecenas accumsan lacus vel facilisis.</p>
    </article>
    <ul class="carousel-dots"><li class="current"></li><li></li><li></li><li></li></ul>
  </div>
</section>

<!-- By craft -->
<h2 class="section-label" style="top:1549px">BY CRAFT</h2>
<section class="panel" style="top:1596px">
  <aside class="sidebar">
    <div class="brand"><span class="brand-dot"></span><span class="brand-name">MIREL VOSS</span></div>
    <ul class="nav">
      <li style="top:128px">HOME</li>
      <li style="top:166px">WHO AM I</li>
      <li style="top:203px">WHAT I DO<svg width="8" height="5" viewBox="0 0 8 5"><path d="M1 1l3 3 3-3" fill="none" stroke="#fff" stroke-width="1.2"/></svg></li>
      <li class="sub" style="top:241px">BY BRAND</li>
      <li class="sub active" style="top:278px">BY CRAFT</li>
      <li style="top:316px">HOW TO REACH ME</li>
    </ul>
    <span class="social" style="left:39px;top:354px"></span>
  </aside>
  <div class="main">
    <h1 class="page-title">BY <span class="accent">CRAFT</span></h1>
    <p class="subhead">Kestrel Systems</p>
    <article class="project" style="left:63px">
      <div class="project-media" role="img" aria-label="Project image: screenshot of an advertising video gallery page" style="background:linear-gradient(180deg,#c8102e 0%,#c8102e 6%,#e4e4e4 7%,#f6f6f6 20%,#4a4a4a 36%,#4a4a4a 62%,#f6f6f6 64%,#e8e8e8 100%)"></div>
      <h3 class="project-title">Project One</h3>
      <p class="project-text">Lorem ipsum dolor sit amet, consectetur adipiscing elit, sed do eiusmod tempor incididunt ut labore et dolore magna aliqua. Quis ipsum suspendisse ultrices gravida. Risus commodo viverra maecenas accumsan lacus vel facilisis.</p>
    </article>
    <article class="project" style="left:394px">
      <div class="project-media" role="img" aria-label="Project image: screenshot of a Japanese office software store page" style="background:linear-gradient(180deg,#ffffff 0%,#ffffff 13%,#e2231a 14%,#e2231a 16%,#e5e5e5 17%,#e5e5e5 40%,#ffffff 41%,#ffffff 100%)"></div>
      <h3 class="project-title">Project Two</h3>
      <p class="project-text">Lorem ipsum dolor sit amet, consectetur adipiscing elit, sed do eiusmod tempor incididunt ut labore et dolore magna aliqua. Quis ipsum suspendisse ultrices gravida. Risus commodo viverra maecenas accumsan lacus vel facilisis.</p>
    </article>
    <ul class="carousel-dots"><li class="current"></li><li></li><li></li><li></li></ul>
  </div>
</section>

</body>
</html>
```